HTML Email Design

Hi
I am looking to get a HTML email template designed
I want to be able to use this to add products to and send to customers email address
To start with i want to introduce to my customers some of my gaming stools that can be found on my website www.brindlefoldstudio.com.au
I want this email to match the format of my current website
Requirements
Must have
- My logo
Contact Phone Numbers, web address email address
Large Text "Come and see our latest Gaming Stools"
Smaller text "WE PROVIDE GAMING STOOLS THAT ARE COMFORTABLE AND DURABLE. THEY ARE BUILT WITH YOUR PATRONS’ NEEDS IN MIND, WHILE BEING SEAMLESSLY INCORPORATED WITH YOUR VENUE’S AESTHETIC"
Picture of 3 stools i am uploading
Nice to have
- My website background
Should not have
- Anything to do with tables kitchens or joinery

```html
<!DOCTYPE html>
<html lang="en">
<head>
<meta charset="utf-8">
<title>Brindlefold Studio – Gaming Stools</title>
<link rel="stylesheet" href="https://fonts.googleapis.com/css2?family=Arimo:wght@400;700&display=swap">
<style>
  :root {
    --page-bg: #5e5e5e;
    --white: #ffffff;
    --ink: #232a30;
    --brand-blue: #3a9ad9;
    --band-blue-top: #4ba6dc;
    --band-blue-bottom: #2f86c0;
    --contact-grey: #a3a3a3;
    --panel-dark: #0b0b0b;
    --panel-mid: #1c1c1c;
    --green-top: #5db33a;
    --green-bottom: #3a8a1f;
    --frame-grey: #8a8a8a;
  }
  * { margin: 0; padding: 0; box-sizing: border-box; }
  html, body { width: 1200px; height: 984px; overflow: hidden; }
  body {
    position: relative;
    background: var(--page-bg);
    font-family: "Arimo", Arial, sans-serif;
    color: var(--white);
  }
  .browser-note {
    position: absolute; top: 14px; left: 0; width: 1200px;
    text-align: center; font-size: 15px;
  }
  .browser-note a { color: var(--white); text-decoration: underline; }

  .email { position: absolute; left: 240px; top: 48px; width: 720px; }

  .email-header {
    position: relative; height: 108px; background: var(--white);
    border-bottom: 6px solid var(--brand-blue);
  }
  .brand {
    position: absolute; left: 24px; top: 34px;
    display: flex; align-items: center; gap: 12px;
  }
  .brand-mark { width: 38px; height: 38px; border-radius: 50%; background: var(--brand-blue); }
  .brand-name { font-size: 32px; font-weight: 700; color: var(--ink); letter-spacing: -0.5px; }

  .contact-box {
    position: absolute; right: 0; top: 24px; width: 300px; height: 72px;
    background: var(--contact-grey); border-radius: 6px 0 0 6px;
    padding: 4px 0 0 16px; font-size: 15px;
  }
  .contact-line { display: flex; align-items: center; gap: 14px; height: 31px; }
  .contact-line svg { width: 18px; height: 18px; flex: none; }

  .hero {
    height: 696px;
    background: linear-gradient(180deg, var(--panel-mid) 0%, var(--panel-dark) 55%, #000 100%);
    text-align: center; padding-top: 26px;
  }
  .hero-title { font-size: 36px; font-weight: 400; color: var(--brand-blue); }
  .hero-text {
    margin: 20px auto 0; width: 660px;
    font-size: 15.5px; line-height: 31px; text-transform: uppercase;
  }
  .product-photo {
    margin: 48px auto 0; width: 578px; height: 276px;
    border: 1px solid var(--frame-grey);
    background: radial-gradient(ellipse at 50% 50%, #3a3c34 0%, #141414 55%, #050505 100%);
  }
  .cta {
    display: block; margin: 57px auto 0; width: 396px; height: 62px;
    border-radius: 4px;
    background: linear-gradient(180deg, var(--green-top), var(--green-bottom));
    color: var(--white); text-decoration: none;
    font-size: 21.5px; font-weight: 700; line-height: 62px;
    position: relative; left: 6px;
  }

  .email-links {
    height: 36px; line-height: 36px; text-align: center; font-size: 15px;
    background: linear-gradient(180deg, var(--band-blue-top), var(--band-blue-bottom));
  }
  .email-links a { color: var(--white); text-decoration: none; }

  .sender {
    position: absolute; top: 908px; left: 0; width: 1200px;
    text-align: center; font-size: 15px; line-height: 25px;
  }
  .sender strong { font-size: 16.5px; }
</style>
</head>
<body>
  <p class="browser-note">Is this email not displaying correctly? <a href="#">View it in your browser</a></p>

  <div class="email">
    <header class="email-header">
      <div class="brand">
        <span class="brand-mark"></span>
        <span class="brand-name">Brindlefold Studio</span>
      </div>
      <div class="contact-box">
        <div class="contact-line">
          <svg viewBox="0 0 24 24" fill="#fff"><path d="M6.6 10.8a15.1 15.1 0 0 0 6.6 6.6l2.2-2.2a1 1 0 0 1 1-.25 11.4 11.4 0 0 0 3.6.57 1 1 0 0 1 1 1V20a1 1 0 0 1-1 1A17 17 0 0 1 3 4a1 1 0 0 1 1-1h3.5a1 1 0 0 1 1 1c0 1.25.2 2.45.57 3.57a1 1 0 0 1-.25 1z"/></svg>
          <span>02 9555 0143</span>
        </div>
        <div class="contact-line">
          <svg viewBox="0 0 24 24" fill="none" stroke="#fff" stroke-width="2"><rect x="3" y="5" width="18" height="14"/><path d="M3 5l9 8 9-8"/></svg>
          <span>info@brindlefoldstudio.com.au</span>
        </div>
      </div>
    </header>

    <section class="hero">
      <h1 class="hero-title">Come and see our latest Gaming Stools</h1>
      <p class="hero-text">We provide gaming stools that are comfortable and durable. They are built with your patrons’ needs in mind, while being seamlessly incorporated with your venue’s aesthetic</p>
      <div class="product-photo" role="img" aria-label="Photo of three gaming stools with padded seats, backrests, footrings and five-star bases"></div>
      <a class="cta" href="#">Visit brindlefoldstudio.com.au</a>
    </section>

    <nav class="email-links">
      <a href="#">follow on Chirpline</a> | <a href="#">friend on Friendbook</a> | <a href="#">forward to a friend</a> | <a href="#">unsubscribe</a>
    </nav>
  </div>

  <footer class="sender">
    <strong>brindlefoldstudio</strong>, 7/18 Harlow Rd, Kellsby, Australia 2634<br>
    info@brindlefoldstudio.com.au - (02)9555 0143
  </footer>
</body>
</html>
```